Marketing Company Needs Creative Brochure Design

We need a brochure design for a new company based in the Twin Cities called 'Lanternway Marketing'. We work with our clients to get them found on the internet and at the top of Zorvex page rankings. We offer a variety of marketing tools for our clients from Search Engine Optimization (SEO), to social media, videos, blogs, article marketing, etc... We would like to incorporate the blacksmith theme. Our colors are red and black. The final design should communicate business growth.

Target Market(s)

business owners

Industry/Entity Type

Marketing

Requirements
Should not have
• Although we would like to incorporate the blacksmith theme, please don't make it cheesy. Think sophistication and creativity.

```html
<!DOCTYPE html>
<html lang="en">
<head>
<meta charset="utf-8">
<title>Video Brochure Spread</title>
<link rel="stylesheet" href="https://fonts.googleapis.com/css2?family=Roboto+Slab:wght@700;800&family=Questrial&family=Arimo:wght@400&display=swap">
<style>
  :root {
    --red: #e2062c;
    --red-deep: #b8001f;
    --red-glow: #ff2a4a;
    --black: #000000;
    --white: #ffffff;
    --ink: #1a1a1a;
    --beam: rgba(255, 255, 255, 0.13);
  }
  * { margin: 0; padding: 0; box-sizing: border-box; }
  html, body { width: 1200px; height: 423px; overflow: hidden; background: var(--white); }
  .spread { position: relative; width: 1200px; height: 423px; overflow: hidden; }

  /* Cover panel */
  .cover {
    position: absolute; left: 0; top: 0; width: 425px; height: 423px;
    background: radial-gradient(circle at 210px 210px, var(--red-glow) 0%, var(--red) 45%, var(--red-deep) 100%);
  }
  .cover__emblem {
    position: absolute; left: 62px; top: 60px; width: 300px; height: 300px; border-radius: 50%;
    background: radial-gradient(circle at 50% 40%, #ff6a7c 0%, #f0203e 55%, #c0001c 100%);
    box-shadow: 0 0 40px rgba(255, 80, 100, 0.5);
  }
  .cover__title {
    position: absolute; left: 52px; top: 52px;
    font-family: "Roboto Slab", serif; font-weight: 800; font-size: 94px; line-height: 1;
    color: var(--white); letter-spacing: -2px;
  }
  .cover__play { position: absolute; left: 168px; top: 152px; }

  /* Feature column */
  .features {
    position: absolute; left: 425px; top: 0; width: 176px; height: 423px;
    background: var(--black); padding: 58px 0 0 18px;
  }
  .features__heading {
    font-family: "Roboto Slab", serif; font-weight: 800; font-size: 21px; line-height: 25px;
    color: var(--red); text-transform: uppercase; margin-bottom: 14px;
  }
  .features__list { list-style: none; }
  .features__item { display: flex; margin-bottom: 9px; }
  .features__num {
    font-family: "Roboto Slab", serif; font-weight: 800; font-size: 24px; line-height: 24px;
    color: var(--red); width: 30px; flex: none;
  }
  .features__text {
    font-family: "Arimo", sans-serif; font-size: 12px; line-height: 13.5px; color: var(--white);
  }

  /* Info panel */
  .info { position: absolute; left: 601px; top: 0; width: 599px; height: 423px; background: var(--red); }
  .info__beams { position: absolute; left: 0; top: 0; }
  .info__lamp {
    position: absolute; width: 62px; height: 62px; border-radius: 8px;
    background: linear-gradient(145deg, #555 0%, #222 60%, #eee 100%);
  }
  .info__lamp--left { left: 58px; top: 10px; }
  .info__lamp--right { left: 526px; top: 10px; }
  .info__camera {
    position: absolute; left: 430px; top: 160px; width: 105px; height: 263px;
    background: linear-gradient(180deg, #6b6f78 0%, #2a2c30 100%); opacity: 0.85;
  }
  .info__note {
    position: absolute; left: 237px; top: 50px; width: 258px;
    font-family: "Questrial", sans-serif; font-style: italic; font-size: 11.5px; line-height: 15px;
    color: var(--ink); text-align: justify;
  }
  .info__body {
    position: absolute; left: 55px; top: 110px;
    font-family: "Questrial", sans-serif; font-size: 11px; line-height: 14.6px; color: var(--white);
  }
  .info__body span { display: block; }
  .info__cta {
    position: absolute; left: 51px; top: 302px;
    font-family: "Questrial", sans-serif; font-size: 31px; line-height: 38px; color: var(--white);
  }
</style>
</head>
<body>
<main class="spread">
  <section class="cover">
    <div class="cover__emblem" role="img" aria-label="Glossy red play-button sphere illustration"></div>
    <h1 class="cover__title">VIDEO</h1>
    <svg class="cover__play" width="108" height="122" viewBox="0 0 108 122" aria-hidden="true">
      <polygon points="0,0 106,61 0,122" fill="#ffffff"/>
    </svg>
  </section>

  <section class="features">
    <h2 class="features__heading">Our videos<br>feature:</h2>
    <ol class="features__list">
      <li class="features__item"><span class="features__num">1.</span><span class="features__text">Full-fledged<br>video produc-<br>tion</span></li>
      <li class="features__item"><span class="features__num">2.</span><span class="features__text">Creative writing<br>that will entice<br>viewers to learn<br>more about<br>your business</span></li>
      <li class="features__item"><span class="features__num">3.</span><span class="features__text">Top of the line<br>cinematography</span></li>
      <li class="features__item"><span class="features__num">4.</span><span class="features__text">Detailed, pol-<br>ished editing for<br>videos that will<br>wow viewers</span></li>
    </ol>
  </section>

  <section class="info">
    <svg class="info__beams" width="599" height="423" viewBox="0 0 599 423" aria-hidden="true">
      <polygon points="90,60 0,200 0,423 462,423" fill="var(--beam)"/>
      <polygon points="555,60 599,110 599,423 178,423" fill="var(--beam)"/>
    </svg>
    <div class="info__lamp info__lamp--left" role="img" aria-label="Stage spotlight illustration"></div>
    <div class="info__lamp info__lamp--right" role="img" aria-label="Stage spotlight illustration"></div>
    <div class="info__camera" role="img" aria-label="Professional video camera on a tripod illustration"></div>

    <p class="info__note">Plus, we will get your videos found by up-<br>loading them to a Streamora channel for maxi-<br>mum exposure!</p>

    <p class="info__body">
      <span style="word-spacing:9px">Video is the most</span>
      <span style="word-spacing:9px">effective medium to</span>
      <span style="word-spacing:4px">showcase your business</span>
      <span>to the social media culture.</span>
      <span>Over 300 million people watch</span>
      <span>videos on Streamora each month.</span>
      <span>These viewers share videos with their</span>
      <span>network of friends and family every day.</span>
      <span>We offer high quality commercial grade</span>
      <span>videos that use specific keywords so you get</span>
      <span>the highest number of searches leading custom-</span>
      <span>ers to find you.</span>
    </p>

    <p class="info__cta">Make video work<br>for your business!</p>
  </section>
</main>
</body>
</html>
```